2025 Fall Auction

Large Farm and construction online only auction November 3rd thru 5Th
Bidding Closes November 5 th at 7 pm
Now Accepting Consignment call ( 555 )-271-6038 or email Marcus@brevlandsales.com
150 + Skid Steer Attachments
50 + Pieces of farm equipment
More To Come
Consignments are welcomed Till October 25Th

Target Market(s)

New customers

```html
<!DOCTYPE html>
<html lang="en">
<head>
<meta charset="utf-8">
<title>Large Farm &amp; Construction Auction</title>
<link href="https://fonts.googleapis.com/css2?family=League+Gothic&family=Outfit:wght@300;400;500;600&display=swap" rel="stylesheet">
<style>
  :root {
    --orange: #f7931e;
    --ink: #111111;
    --paper: #fbfbfb;
    --grey: #9c9c9c;
    --grey-light: #d9d9d9;
    --muted: #a3a3a3;
    --white: #ffffff;
  }
  html, body { margin: 0; padding: 0; overflow: hidden; background: var(--paper); }
  .flyer {
    position: relative; width: 1200px; height: 1200px; overflow: hidden;
    background: var(--paper);
    font-family: "Outfit", sans-serif; color: var(--ink);
  }
  .headline { position: absolute; left: 0; top: 0; width: 720px; height: 440px; }
  .headline text { font-family: "League Gothic", sans-serif; }
  .headline .line-farm { fill: var(--orange); font-size: 224px; }
  .headline .line-construction { fill: var(--ink); font-size: 176px; }

  .date-tag {
    position: absolute; left: 140px; top: 414px; width: 494px; height: 146px;
    background: var(--orange); transform: rotate(-3.4deg); transform-origin: left top;
    color: var(--white); box-sizing: border-box; padding: 26px 0 0 28px;
    font-weight: 500; font-size: 36px; line-height: 50px; letter-spacing: -0.3px;
  }
  .date-tag .fold {
    position: absolute; right: 0; top: 0; width: 0; height: 0;
    border-style: solid; border-width: 0 34px 34px 0;
    border-color: transparent var(--paper) #f6d6a8 transparent;
  }

  .closing { position: absolute; left: 89px; top: 623px; }
  .closing .marker {
    position: absolute; left: 0; top: 9px; width: 0; height: 0;
    border-style: solid; border-width: 10px 0 10px 18px;
    border-color: transparent transparent transparent var(--orange);
  }
  .closing p { margin: 0 0 0 38px; font-size: 34px; line-height: 50px; letter-spacing: -0.4px; }
  .closing .label { font-weight: 300; }
  .closing .when { font-weight: 500; }

  .stats { position: absolute; left: 89px; top: 760px; }
  .stat { position: absolute; top: 0; width: 260px; }
  .stat-farm { left: 295px; }
  .stat .figure { margin: 0; color: var(--orange); font-weight: 600; font-size: 92px; line-height: 92px; letter-spacing: -3px; }
  .stat .caption { margin: 20px 0 0; font-weight: 300; font-size: 30px; line-height: 44px; letter-spacing: -0.3px; }
  .stats .divider { position: absolute; left: 249px; top: 14px; width: 3px; height: 183px; background: var(--ink); }

  .more-to-come {
    position: absolute; left: 89px; top: 1010px; margin: 0;
    font-size: 34px; line-height: 52px; font-weight: 400; letter-spacing: -0.4px;
  }
  .more-to-come .soft { color: var(--muted); }
  .more-to-come .strong { color: var(--ink); font-weight: 500; }

  .equipment-photo {
    position: absolute; left: 710px; top: -50px; width: 1000px; height: 1000px; border-radius: 50%;
    background: linear-gradient(180deg, #e6e8ec 0%, #d5d8dd 40%, #b9b5ae 60%, #6f6a64 78%, #3d3b39 100%);
  }

  .brand-card {
    position: absolute; left: 799px; top: 0; width: 315px; height: 366px;
    background: var(--white); border-radius: 0 0 14px 14px;
  }
  .brand-card .brand-dot {
    position: absolute; left: 67px; top: 70px; width: 180px; height: 180px;
    border-radius: 50%; background: var(--orange);
  }
  .brand-card .brand-name {
    position: absolute; left: 0; right: 0; top: 268px; text-align: center; margin: 0;
    font-family: "League Gothic", sans-serif; font-size: 52px; line-height: 52px;
    color: var(--orange); letter-spacing: 0.5px;
  }

  .consign-card {
    position: absolute; left: 719px; top: 843px; width: 391px; height: 267px;
    background: var(--grey); color: var(--white); box-sizing: border-box; padding: 36px 0 0 36px;
  }
  .consign-card .fold {
    position: absolute; right: 0; top: 0; width: 0; height: 0; border-style: solid;
    border-width: 0 44px 44px 0; border-color: transparent var(--paper) var(--grey-light) transparent;
  }
  .consign-card .heading { margin: 0; font-weight: 300; font-size: 33px; line-height: 45px; letter-spacing: -0.3px; }
  .contact-row { display: flex; align-items: center; margin-top: 0; }
  .contact-row.phone { margin-top: 30px; font-size: 33px; font-weight: 500; letter-spacing: -0.5px; }
  .contact-row.email { margin-top: 12px; font-size: 23px; font-weight: 500; }
  .contact-row svg { width: 30px; height: 30px; margin-right: 22px; fill: var(--white); flex: none; }
</style>
</head>
<body>
<main class="flyer">
  <svg class="headline" viewBox="0 0 720 440" aria-label="Large Farm &amp; Construction">
    <text class="line-farm" x="86" y="254" textLength="534" lengthAdjust="spacingAndGlyphs">LARGE FARM</text>
    <text class="line-construction" x="84" y="414" textLength="587" lengthAdjust="spacingAndGlyphs">&amp; CONSTRUCTION</text>
  </svg>

  <div class="date-tag">
    <span class="fold"></span>
    Online Only Auction<br>Nov 3rd - 5th
  </div>

  <div class="closing">
    <span class="marker"></span>
    <p class="label">Bidding Closes</p>
    <p class="when">Novemeber 5th at 7 pm</p>
  </div>

  <section class="stats">
    <div class="stat stat-attachments">
      <p class="figure">150+</p>
      <p class="caption">Skid Steer<br>Attachments</p>
    </div>
    <span class="divider"></span>
    <div class="stat stat-farm">
      <p class="figure">50+</p>
      <p class="caption">Pieces of farm<br>equipment</p>
    </div>
  </section>

  <p class="more-to-come"><span class="soft">More to Come Consignment</span><br><span class="soft">are</span> <span class="strong">Welcomed till Oct 25Th</span></p>

  <div class="equipment-photo" role="img" aria-label="Photo of a large white and orange four-wheel-drive tractor with dual tires parked by a farm shed"></div>

  <div class="brand-card">
    <span class="brand-dot"></span>
    <p class="brand-name">BREVLAND SALES</p>
  </div>

  <aside class="consign-card">
    <span class="fold"></span>
    <p class="heading">Now Accepting<br>Consignment Call</p>
    <div class="contact-row phone">
      <svg viewBox="0 0 24 24" aria-hidden="true"><path d="M6.6 10.8a15.2 15.2 0 0 0 6.6 6.6l2.2-2.2a1 1 0 0 1 1-.25 11.4 11.4 0 0 0 3.6.57 1 1 0 0 1 1 1V20a1 1 0 0 1-1 1A17 17 0 0 1 3 4a1 1 0 0 1 1-1h3.5a1 1 0 0 1 1 1c0 1.25.2 2.45.57 3.6a1 1 0 0 1-.25 1z"/></svg>
      <span>(555)-271-6038</span>
    </div>
    <div class="contact-row email">
      <svg viewBox="0 0 24 24" aria-hidden="true"><path d="M2 5h20v2l-10 6L2 7z"/><path d="M2 9l10 6 10-6v10H2z"/></svg>
      <span>Marcus@brevlandsales</span>
    </div>
  </aside>
</main>
</body>
</html>
```